Data Visualization (graphs, tables, models, circles)

We need an intuitive - user friendly - and fresh design line for our data visualization.

You know. Keep The Page Calm!

Our core product is based on the presentation and interpretation of different data sources that we combine into graphs, tables, charts etc and make visible to clients through a web platform and or Reports. Our business area is Search & Social Media Intelligence.

See Vantrel.com for some inspiration in terms of current colors and a better understanding of the company. Our Logo / Name is the only one thing that cannot be changed. Everything else is up to you. Feel free to ask questions.

I have attached a few screenshots of some of our features and as you can see - there has never been a designer on this assignment. We are looking for a long term relationship with a designer that can work with us on an ongoing basis.

Design of graphs/models/circles/tables needs to be able to fit into Infographics also.

We are basically looking for an identity for our data visualization. Meaning that readers / target audience can recognize our graphs and say: Check out the cool graphs by Vantrel :-)

Think: Plorvex, TallyNorth, etc. in terms of data presentation.
Updates

Project Deadline Extended
Reason: Due to illness we lost a few days last week and have not have sufficient time to look through the different designs.

Target Market(s)

Marketing People, CEO's, Strategic Planners, Ad Agencies, Decision Makers

Industry/Entity Type

Business

Requirements
Must have
• Must present at least 1 line graph (like file 1 and 2), 1 pie chart, 1 column graph and 1 matrix (like file3).

```html
<!DOCTYPE html>
<html lang="en">
<head>
<meta charset="utf-8">
<title>SEO Battle Card – Universal Search</title>
<link rel="stylesheet" href="https://fonts.googleapis.com/css2?family=Montserrat:wght@300;400&display=swap">
<style>
  :root {
    --paper: #eeeff1;
    --brand-red: #c8142a;
    --rule: #e58a7c;
    --y2012: #c71428;
    --y2011: #d66e5e;
    --y2010: #e09b8a;
    --axis: #6d6e71;
    --label: #77787b;
    --seg-dark: #87888b;
    --seg-mid: #a8a9ac;
    --seg-pale: #c3c4c6;
    --seg-light: #ffffff;
  }
  html, body {
    margin: 0;
    padding: 0;
    overflow: hidden;
    background: var(--paper);
  }
  .battle-card {
    position: relative;
    width: 1200px;
    height: 984px;
    background: var(--paper);
    font-family: "Montserrat", Arial, sans-serif;
    overflow: hidden;
  }
  .card-title {
    position: absolute;
    left: 155px;
    top: 88px;
    margin: 0;
    font-size: 24px;
    font-weight: 300;
    color: var(--brand-red);
    white-space: nowrap;
  }
  .rule {
    position: absolute;
    left: 101px;
    width: 968px;
    height: 1px;
    background: var(--rule);
  }
  .rule--top { top: 131px; }
  .rule--bottom { top: 880px; }
  .card-footer {
    position: absolute;
    left: 101px;
    top: 896px;
    margin: 0;
    font-size: 12.5px;
    color: var(--brand-red);
    white-space: nowrap;
  }
  .chart {
    position: absolute;
    left: 0;
    top: 0;
  }
  .axis-line { stroke: var(--axis); stroke-width: 1.2; }
  .axis-dot { fill: var(--axis); }
  .tick-label { font-size: 13px; fill: var(--label); text-anchor: end; font-weight: 300; }
  .value-label { font-size: 12.5px; fill: var(--label); text-anchor: middle; }
  .category-label { font-size: 13px; fill: var(--label); text-anchor: middle; }
  .legend-label { font-size: 11px; fill: var(--label); }
  .donut-label { font-size: 12px; fill: var(--label); text-anchor: middle; }
  .bar--2012, .dot--2012 { fill: var(--y2012); }
  .bar--2011, .dot--2011 { fill: var(--y2011); }
  .bar--2010, .dot--2010 { fill: var(--y2010); }
  .seg { fill: none; stroke-width: 25; stroke-linecap: butt; }
  .seg--2012 { stroke: var(--y2012); }
  .seg--2011 { stroke: var(--y2011); }
  .seg--2010 { stroke: var(--y2010); }
  .seg--dark { stroke: var(--seg-dark); }
  .seg--mid { stroke: var(--seg-mid); }
  .seg--pale { stroke: var(--seg-pale); }
  .seg--light { stroke: var(--seg-light); }
</style>
</head>
<body>
<main class="battle-card">
  <h1 class="card-title">SEO Battle Card - Universal Search</h1>
  <div class="rule rule--top"></div>

  <svg class="chart" width="1200" height="984" viewBox="0 0 1200 984" aria-label="Share of search result types 2010–2012">
    <g class="legend">
      <circle class="dot--2012" cx="1017" cy="157" r="5"/>
      <text class="legend-label" x="1033" y="161">2012</text>
      <circle class="dot--2011" cx="1017" cy="172" r="5"/>
      <text class="legend-label" x="1033" y="176">2011</text>
      <circle class="dot--2010" cx="1017" cy="187" r="5"/>
      <text class="legend-label" x="1033" y="191">2010</text>
    </g>

    <g class="y-axis">
      <line class="axis-line" x1="237" y1="181" x2="237" y2="808"/>
      <circle class="axis-dot" cx="237" cy="181" r="2.5"/>
      <circle class="axis-dot" cx="237" cy="243.7" r="2.5"/>
      <circle class="axis-dot" cx="237" cy="306.4" r="2.5"/>
      <circle class="axis-dot" cx="237" cy="369.1" r="2.5"/>
      <circle class="axis-dot" cx="237" cy="431.8" r="2.5"/>
      <circle class="axis-dot" cx="237" cy="494.5" r="2.5"/>
      <circle class="axis-dot" cx="237" cy="557.2" r="2.5"/>
      <circle class="axis-dot" cx="237" cy="619.9" r="2.5"/>
      <circle class="axis-dot" cx="237" cy="682.6" r="2.5"/>
      <circle class="axis-dot" cx="237" cy="745.3" r="2.5"/>
      <text class="tick-label" x="215" y="186">100%</text>
      <text class="tick-label" x="215" y="249">90%</text>
      <text class="tick-label" x="215" y="312">80%</text>
      <text class="tick-label" x="215" y="374">70%</text>
      <text class="tick-label" x="215" y="436">60%</text>
      <text class="tick-label" x="215" y="502">50%</text>
      <text class="tick-label" x="215" y="565">40%</text>
      <text class="tick-label" x="215" y="626">30%</text>
      <text class="tick-label" x="215" y="690">20%</text>
      <text class="tick-label" x="215" y="752">10%</text>
      <text class="tick-label" x="215" y="811">0%</text>
    </g>

    <g class="x-axis">
      <line class="axis-line" x1="237" y1="808" x2="893" y2="808"/>
      <circle class="axis-dot" cx="237" cy="808" r="2.5"/>
      <circle class="axis-dot" cx="398" cy="808" r="2.5"/>
      <circle class="axis-dot" cx="555" cy="808" r="2.5"/>
      <circle class="axis-dot" cx="713" cy="808" r="2.5"/>
      <circle class="axis-dot" cx="872" cy="808" r="2.5"/>
      <text class="category-label" x="316" y="833">Classic</text>
      <text class="category-label" x="477" y="833">Images</text>
      <text class="category-label" x="642" y="840">Video</text>
      <text class="category-label" x="793" y="840">Shopping</text>
    </g>

    <g class="group group--classic">
      <rect class="bar--2012" x="267" y="209" width="32" height="599"/>
      <rect class="bar--2011" x="301" y="272" width="32" height="536"/>
      <rect class="bar--2010" x="335" y="372" width="32" height="436"/>
      <text class="value-label" x="283" y="205">96%</text>
      <text class="value-label" x="317" y="268">86%</text>
      <text class="value-label" x="351" y="368">60%</text>
    </g>

    <g class="group group--images">
      <rect class="bar--2012" x="425" y="790" width="32" height="18"/>
      <rect class="bar--2011" x="459" y="759" width="32" height="49"/>
      <rect class="bar--2010" x="493" y="715" width="32" height="93"/>
      <text class="value-label" x="441" y="786">3%</text>
      <text class="value-label" x="475" y="755">8%</text>
      <text class="value-label" x="509" y="711">15%</text>
    </g>

    <g class="group group--video">
      <rect class="bar--2012" x="583" y="804" width="32" height="4"/>
      <rect class="bar--2011" x="617" y="778" width="32" height="30"/>
      <rect class="bar--2010" x="651" y="761" width="32" height="47"/>
      <text class="value-label" x="599" y="800">1%</text>
      <text class="value-label" x="633" y="774">5%</text>
      <text class="value-label" x="667" y="757">8%</text>
    </g>

    <g class="group group--shopping">
      <rect class="bar--2011" x="767" y="802" width="32" height="6"/>
      <rect class="bar--2010" x="801" y="766" width="32" height="42"/>
      <text class="value-label" x="746" y="805">0%</text>
      <text class="value-label" x="783" y="797">1%</text>
      <text class="value-label" x="817" y="762">7%</text>
    </g>

    <g class="donut donut--2012">
      <path class="seg seg--2012" d="M588 294.5 A62.5 62.5 0 1 1 571.30 296.77"/>
      <path class="seg seg--mid" d="M572.35 296.49 A62.5 62.5 0 0 1 582.55 294.74"/>
      <path class="seg seg--pale" d="M583.64 294.65 A62.5 62.5 0 0 1 587.45 294.50"/>
      <text class="donut-label" x="588" y="361">2012</text>
    </g>

    <g class="donut donut--2011">
      <path class="seg seg--2011" d="M795 295.5 A62.5 62.5 0 1 1 745.75 319.52"/>
      <path class="seg seg--dark" d="M746.43 318.67 A62.5 62.5 0 0 1 770.58 300.47"/>
      <path class="seg seg--mid" d="M771.59 300.05 A62.5 62.5 0 0 1 787.38 295.97"/>
      <path class="seg seg--light" d="M788.47 295.84 A62.5 62.5 0 0 1 792.82 295.54"/>
      <text class="donut-label" x="795" y="362">2011</text>
    </g>

    <g class="donut donut--2010">
      <path class="seg seg--2010" d="M1000 295.5 A62.5 62.5 0 1 1 945.87 389.25"/>
      <path class="seg seg--dark" d="M945.34 388.30 A62.5 62.5 0 0 1 950.75 319.52"/>
      <path class="seg seg--mid" d="M951.43 318.67 A62.5 62.5 0 0 1 975.58 300.47"/>
      <path class="seg seg--light" d="M976.59 300.05 A62.5 62.5 0 0 1 999.45 295.50"/>
      <text class="donut-label" x="1000" y="362">2010</text>
    </g>
  </svg>

  <div class="rule rule--bottom"></div>
  <p class="card-footer">All images and data are property of Vantrel Technology SA</p>
</main>
</body>
</html>
```